Velmora Packaging Design

We will need a package for our supplement Velmora.

Velmora is the first and only once-a-day nutritional supplement clinically shown to boost Memory, Focus, Concentration and Alertness. It's a safe and natural blend of patented Neuropeptides.

The product formulation was developed by a pharmaceutical company and is a natural over-the-counter supplement based on a successful drug used to aid in brain recovery and repair for stroke and alzheimer's patients.

Supplements (capsules) are blister packed and inserted into the box. We are looking for the box design. Capsules are gray with dark blue print of the name and icon.

Package dimensions are: 4.5"W x 2.875"H x .75"D

See uploaded die line.
Updates

I included a link on the creative brief that will give you the supplement facts and FDA statement.

It is here, too.

https://www.parcelvaultdrop.example/a4529fbd-1e83-47c0-b961-08ac3d2e7f15?rid=QmPxRtLk8WvYcHs2NbG-FjE5

Project Deadline Extended
Reason: We are out of the office for the rest of the week and need to give feedback to refine the designs that have been submitted. We will be eliminating the designs that are off base later today to also provide a strong packaging direction. Thanks.

Target Market(s)

Men and Women 45+ who want to restore and maintain optimal brain function, memory, focus and clarity

Industry/Entity Type

Pharmaceutical

Requirements
Must have
• Must feature our parent brand LunaGrovium logo. See uploaded files.

Copy on front of box should say:

Velmora (there is no logo for Velmora, your design)

*Clinically proven to improve memory,focus and concentration
*Patented blend of Neuropeptides to support healthy brain function

Contains 30 Capsules

Must have Supplemental Facts
Must have FDA disclaimer

The site won't let me upload...but here is a link to download the supplemental facts and fda disclaimer

Nice to have
• "Guaranteed Results In Less Than 30 Days!" in a call out.

Molecule design icon (see upload)

We like the blue, green color palette, but feel free to be creative understanding that this is an all-natural supplement derived from nature but developed by a pharmaceutical company.

```html
<!DOCTYPE html>
<html lang="en">
<head>
<meta charset="utf-8">
<title>Velmora Carton Dieline</title>
<link href="https://fonts.googleapis.com/css2?family=Arimo:wght@400;700&family=PT+Sans:wght@400;700&family=Tinos:wght@400;700&display=swap" rel="stylesheet">
<style>
  :root {
    --stage-light: #ffffff;
    --stage-dark: #d9d9d9;
    --flap: #ffffff;
    --flap-edge: #d0d0d0;
    --leaf-deep: #2f7a12;
    --leaf-mid: #5fa51c;
    --leaf-light: #a9d446;
    --sun: #f4ee2c;
    --pale: #e6efb4;
    --bark: #4a2c1a;
    --mint-text: #d9f6b2;
    --cream-text: #fffbd0;
    --ink: #111111;
    --badge-light: #e9f5ff;
    --badge-mid: #6fb6ee;
    --badge-text: #1f6e12;
  }
  * { box-sizing: border-box; margin: 0; padding: 0; }
  html, body { width: 1200px; height: 1036px; overflow: hidden; }
  body {
    background: radial-gradient(ellipse at 50% 45%, var(--stage-light) 30%, var(--stage-dark) 100%);
    font-family: "PT Sans", Arial, sans-serif;
    position: relative;
  }
  .dieline {
    position: absolute; left: 0; top: 0;
    width: 1127px; height: 973px;
    transform: scale(1.0648);
    transform-origin: 0 0;
  }
  .dieline-art { position: absolute; left: 0; top: 0; }
  .abs { position: absolute; }

  .brand-name {
    font-family: "PT Sans", Arial, sans-serif;
    color: var(--bark);
    font-weight: 400;
    display: flex; align-items: center; gap: 10px;
    white-space: nowrap;
  }
  .brand-mark { background: var(--bark); border-radius: 4px; flex: none; }

  .product-name {
    font-family: "Tinos", Georgia, serif;
    color: #ffffff;
    white-space: nowrap;
    line-height: 1;
  }

  .claim {
    font-family: "Tinos", Georgia, serif;
    font-weight: 700;
    text-align: center;
    line-height: 1.05;
    -webkit-text-stroke: 0.6px var(--leaf-deep);
    paint-order: stroke fill;
    text-shadow: 0 1px 2px rgba(0,60,0,.6);
  }

  /* front panel */
  .front-brand { left: 262px; top: 252px; font-size: 30px; }
  .front-brand .brand-mark { width: 60px; height: 60px; }
  .front-name { left: 208px; width: 332px; top: 368px; text-align: center; font-size: 74px; }
  .front-claim { left: 215px; width: 320px; top: 455px; font-size: 20px; color: var(--mint-text); }
  .front-blend { left: 362px; width: 172px; top: 586px; font-size: 16px; color: var(--cream-text); }
  .front-count { left: 380px; width: 145px; top: 690px; text-align: right; font-family: "Tinos", serif; font-size: 11px; color: #fff; }

  .results-badge {
    left: 224px; top: 562px; width: 126px; height: 126px; border-radius: 50%;
    background: radial-gradient(circle at 40% 35%, var(--badge-light) 0%, #bfe0fb 45%, var(--badge-mid) 100%);
    border: 3px solid #ffffff;
    box-shadow: 0 2px 6px rgba(0,0,0,.3);
    display: flex; align-items: center; justify-content: center;
  }
  .results-badge p {
    transform: rotate(-16deg);
    font-family: "Tinos", Georgia, serif; font-weight: 700;
    font-size: 15px; line-height: 1.05; text-align: center;
    color: var(--badge-text);
  }

  /* top panel */
  .top-name { left: 224px; top: 140px; font-size: 44px; }

  /* side panel */
  .side-brand {
    left: 163px; top: 600px; font-size: 26px;
    transform: translate(-50%, -50%) rotate(-90deg);
  }
  .side-brand .brand-mark { width: 48px; height: 48px; }

  /* spine */
  .spine-count {
    left: 612px; top: 290px; font-family: "Tinos", serif; font-size: 11px; color: #fff;
    transform: translate(-50%, -50%) rotate(90deg); white-space: nowrap;
  }
  .spine-claim {
    left: 583px; top: 540px; width: 300px; font-size: 18px; color: var(--mint-text);
    transform: translate(-50%, -50%) rotate(90deg);
  }

  /* back panel */
  .back-brand { left: 655px; top: 270px; font-size: 11px; gap: 5px; line-height: 1; }
  .back-brand .brand-mark { width: 22px; height: 22px; }
  .back-name { left: 770px; top: 254px; font-size: 50px; }

  .supplement-facts {
    left: 659px; top: 323px; width: 272px;
    background: #fff; border: 2px solid var(--ink);
    font-family: "Arimo", Arial, sans-serif; color: var(--ink);
    padding: 3px 5px 4px;
  }
  .facts-title { font-size: 17px; font-weight: 700; line-height: 1.1; }
  .facts-serving { display: flex; justify-content: space-between; font-size: 7.5px; padding-right: 40px; border-bottom: 5px solid var(--ink); padding-bottom: 2px; }
  .facts-columns { display: flex; gap: 4px; margin-top: 3px; }
  .facts-table { border-collapse: collapse; width: 50%; font-size: 7.2px; }
  .facts-table th { text-align: left; font-weight: 700; border-bottom: 3px solid var(--ink); padding: 1px 0; }
  .facts-table td { border-bottom: 0.6px solid var(--ink); padding: 0.8px 0; line-height: 1.05; }
  .facts-table .num { text-align: right; }
  .facts-table .blend-head td { font-weight: 700; border-bottom: 1px solid var(--ink); padding-top: 8px; }
  .facts-table .blend-item td { padding-left: 4px; }
  .facts-notes { border-top: 3px solid var(--ink); margin-top: 6px; padding-top: 3px; font-size: 5.5px; line-height: 1.3; }

  .back-copy {
    left: 664px; top: 562px; width: 262px;
    font-family: "Tinos", serif; font-size: 6.3px; line-height: 1.3;
    text-align: center; color: var(--ink);
  }
</style>
</head>
<body>
<div class="dieline">
  <svg class="dieline-art" width="1127" height="973" viewBox="0 0 1127 973">
    <defs>
      <radialGradient id="panelGlow" cx="0.55" cy="0.62" r="0.75">
        <stop offset="0" stop-color="var(--sun)"/>
        <stop offset="0.45" stop-color="#c9de2e"/>
        <stop offset="0.8" stop-color="var(--leaf-mid)"/>
        <stop offset="1" stop-color="#3f8a14"/>
      </radialGradient>
      <linearGradient id="sideGlow" x1="0" y1="0" x2="1" y2="0">
        <stop offset="0" stop-color="var(--leaf-deep)"/>
        <stop offset="0.5" stop-color="var(--leaf-light)"/>
        <stop offset="1" stop-color="var(--leaf-mid)"/>
      </linearGradient>
      <linearGradient id="topGlow" x1="0" y1="0" x2="1" y2="1">
        <stop offset="0" stop-color="#4a9418"/>
        <stop offset="0.6" stop-color="var(--leaf-light)"/>
        <stop offset="1" stop-color="#3f8a14"/>
      </linearGradient>
      <linearGradient id="paleBand" x1="0" y1="0" x2="0" y2="1">
        <stop offset="0" stop-color="#cfe08a"/>
        <stop offset="0.75" stop-color="var(--pale)"/>
        <stop offset="1" stop-color="var(--pale)" stop-opacity="0"/>
      </linearGradient>
      <linearGradient id="footBand" x1="0" y1="0" x2="0" y2="1">
        <stop offset="0" stop-color="var(--leaf-mid)" stop-opacity="0"/>
        <stop offset="1" stop-color="var(--leaf-deep)"/>
      </linearGradient>
    </defs>

    <!-- white flaps -->
    <g fill="var(--flap)" stroke="var(--flap-edge)" stroke-width="1" aria-hidden="true">
      <path d="M210 125 V100 Q210 78 232 78 H506 Q528 78 528 100 V125 Z"/>
      <path d="M118 207 L128 128 H198 L208 207 Z"/>
      <path d="M540 207 L550 128 H618 L628 207 Z"/>
      <path d="M118 715 L128 798 H198 L208 715 Z"/>
      <path d="M540 715 L550 798 H618 L628 715 Z"/>
      <path d="M210 715 H528 V822 Q528 845 505 845 H233 Q210 845 210 822 Z"/>
      <path d="M960 220 L1008 236 V690 L960 706 Z"/>
    </g>

    <!-- top panel -->
    <rect x="210" y="125" width="330" height="82" fill="url(#topGlow)" role="img" aria-label="Green leaf pattern background"/>

    <!-- side panel -->
    <rect x="118" y="207" width="90" height="508" fill="url(#sideGlow)" role="img" aria-label="Green leaf pattern background"/>

    <!-- front panel -->
    <g role="img" aria-label="Green and yellow leaf pattern background">
      <rect x="208" y="207" width="332" height="508" fill="url(#panelGlow)"/>
      <rect x="208" y="207" width="332" height="130" fill="url(#paleBand)"/>
      <rect x="208" y="650" width="332" height="65" fill="url(#footBand)"/>
    </g>

    <!-- spine -->
    <rect x="540" y="207" width="88" height="508" fill="url(#sideGlow)" role="img" aria-label="Green leaf pattern background"/>

    <!-- back panel -->
    <g role="img" aria-label="Green and yellow leaf pattern background">
      <rect x="628" y="207" width="332" height="508" fill="url(#panelGlow)"/>
      <rect x="628" y="207" width="332" height="115" fill="url(#paleBand)"/>
      <rect x="628" y="650" width="332" height="65" fill="url(#footBand)"/>
    </g>
  </svg>

  <!-- top panel -->
  <div class="abs product-name top-name">Velmora</div>

  <!-- side panel -->
  <div class="abs brand-name side-brand"><span class="brand-mark"></span>LunaGrovium</div>

  <!-- front panel -->
  <div class="abs brand-name front-brand"><span class="brand-mark"></span>LunaGrovium</div>
  <div class="abs product-name front-name">Velmora</div>
  <p class="abs claim front-claim">Clinically proven<br>to improve memory<br>focus and concentration</p>
  <div class="abs results-badge"><p>Guaranteed<br>Results<br>In Less Than<br>30 Days!</p></div>
  <p class="abs claim front-blend">Patented blend of<br>Neuropeptides<br>to support<br>healthy brain<br>function</p>
  <p class="abs front-count">Contains 30 Capsules</p>

  <!-- spine -->
  <p class="abs spine-count">Contains 30 Capsules</p>
  <p class="abs claim spine-claim">Clinically proven to improve<br>memory focus and concentration</p>

  <!-- back panel -->
  <div class="abs brand-name back-brand"><span class="brand-mark"></span>LunaGrovium</div>
  <div class="abs product-name back-name">Velmora</div>

  <section class="abs supplement-facts">
    <h2 class="facts-title">Supplement Facts</h2>
    <div class="facts-serving"><span>Servings size: 2 tablets</span><span>Servings per container: 30</span></div>
    <div class="facts-columns">
      <table class="facts-table">
        <tr><th>INGREDIENTS</th><th class="num">AMT</th><th class="num">%DV</th></tr>
        <tr><td>Vitamin A</td><td class="num">3500IU</td><td class="num">70%</td></tr>
        <tr><td>Vitamin B6</td><td class="num">2mg</td><td class="num">100%</td></tr>
        <tr><td>Vitamin B12</td><td class="num">10mcg</td><td class="num">166%</td></tr>
        <tr><td>Vitamin C</td><td class="num">60mg</td><td class="num">100%</td></tr>
        <tr><td>Vitamin D</td><td class="num">400IU</td><td class="num">100%</td></tr>
        <tr><td>Vitamin E</td><td class="num">40IU</td><td class="num">133%</td></tr>
        <tr><td>Folic Acid</td><td class="num">400mcg</td><td class="num">100%</td></tr>
        <tr><td>Thiamine</td><td class="num">1.5mg</td><td class="num">100%</td></tr>
        <tr><td>Niacin</td><td class="num">40mg</td><td class="num">200%</td></tr>
        <tr><td>Calcium</td><td class="num">200mg</td><td class="num">20%</td></tr>
        <tr><td>Biotin</td><td class="num">50mcg</td><td class="num">17%</td></tr>
        <tr><td>Riboflavin</td><td class="num">1.5mg</td><td class="num">88%</td></tr>
        <tr><td>Magnesium</td><td class="num">50mg</td><td class="num">13%</td></tr>
      </table>
      <table class="facts-table">
        <tr><th>INGREDIENTS</th><th class="num">AMT</th><th class="num">%DV</th></tr>
        <tr><td>Manganese</td><td class="num">2mg</td><td class="num">100%</td></tr>
        <tr><td>Chromium</td><td class="num">100mcg</td><td class="num">83%</td></tr>
        <tr><td>Copper</td><td class="num">2mg</td><td class="num">100%</td></tr>
        <tr><td>Molybdenum</td><td class="num">75mcg</td><td class="num">100%</td></tr>
        <tr><td>Selenium</td><td class="num">30mcg</td><td class="num">43%</td></tr>
        <tr><td>Iodine</td><td class="num">100mcg</td><td class="num">67%</td></tr>
        <tr><td>Boron</td><td class="num">150mcg</td><td class="num">*</td></tr>
        <tr class="blend-head"><td colspan="2">Proprietary Blend</td><td class="num">1165mg</td></tr>
        <tr class="blend-item"><td colspan="3">Curcumin</td></tr>
        <tr class="blend-item"><td colspan="3">Green Tea Extract</td></tr>
        <tr class="blend-item"><td colspan="3">L-Carnitine</td></tr>
        <tr class="blend-item"><td colspan="3">Ginseng Extract</td></tr>
      </table>
    </div>
    <p class="facts-notes">*Daily Value Not Established<br>Percent Daily Value Are Based On A 2000 Calorie Diet</p>
  </section>

  <p class="abs back-copy">Lorem ipsum dolor sit amet, consectetur adipiscing elit.<br>Cras sed mauris nulla. Donec nec dolor metus.<br>Nullam varius venenatis dolor, a dignissim mi ullamcorper sed. Donec convallis,<br>diam quis dignissim sagittis, mi ligula lacinia sem,<br>nec dictum eros erat eu velit.<br>Curabitur id nisi quis libero facilisis dignissim ut eu eros.<br>Morbi cursus dui id tellus dapibus a vehicula ipsum adipiscing. Nam id neque sit amet augue<br>vulputate convallis non ac metus. Pellentesque fermentum ullamcorper turpis,<br>et vehicula est dapibus quis. Duis semper rutrum nulla sed aliquam.</p>
</div>
</body>
</html>
```